We need a fresh, new church business card!!

We need a church business card with basic info to hand out as invites. We are looking for something clean that communicates our basic information clearly.

We are open to square or rectangle card sizes.

General Public

Religious

The attached logo is the only one that I have available. We'd like to see options with with text of the logo lighter and on a dark background as well as options with white/light backgrounds.

Also, we'd like to see option with rounded corners.

• Address - 2718 Maple Row, Rockford, IL 61142
• Website - brookvane.example
• Phone - 815-555-0163
• Service times -
• Sunday - 10am Sunday School
• - 11am Family Worship
• - 6pm Night of Prayer
• Wednesday - 7:30pm Adult Bible Study
• Classes for all ages

```html
<!DOCTYPE html>
<html lang="en">
<head>
<meta charset="utf-8">
<title>Brookvane Pentecostal Church – Business Cards</title>
<link rel="stylesheet" href="https://fonts.googleapis.com/css2?family=Baloo+2:wght@500&family=Arimo:wght@400&display=swap">
<style>
  :root {
    --teal: #4f8e9e;
    --teal-light: #7fb1be;
    --ink: #4a4a4a;
    --paper: #ffffff;
    --backdrop: #e9e6e1;
    --rule: #6aa3b1;
  }
  * { box-sizing: border-box; margin: 0; padding: 0; }
  html, body {
    width: 1200px; height: 738px; overflow: hidden;
    background: var(--backdrop);
  }
  .stage { position: relative; width: 1200px; height: 738px; }

  .card {
    position: absolute; width: 540px; height: 315px;
    background: var(--paper); overflow: hidden;
    box-shadow: 0 6px 18px rgba(0,0,0,.18);
    font-family: "Arimo", Arial, sans-serif; color: var(--ink);
  }
  .card--front { left: 50px; top: 60px; }
  .card--back { left: 610px; top: 363px; }

  .side-panel { position: absolute; top: 0; bottom: 0; background: var(--teal); }
  .card--front .side-panel { left: 0; width: 190px; }
  .card--back .side-panel { right: 0; width: 118px; }
  .side-panel__disc {
    position: absolute; width: 190px; height: 190px; border-radius: 50%;
    background: var(--teal-light); opacity: .45;
  }
  .card--front .side-panel__disc { left: -40px; top: 140px; }
  .card--back .side-panel__disc { left: 10px; top: 120px; }

  .wordmark { position: absolute; display: flex; align-items: center; gap: 10px;
    font-family: "Baloo 2", "Trebuchet MS", sans-serif; font-weight: 500; color: var(--teal); }
  .wordmark__dot { width: 30px; height: 30px; border-radius: 50%; background: var(--teal); flex: none; }
  .wordmark__name { font-size: 30px; line-height: 1; letter-spacing: .5px; }
  .wordmark__sub { font-size: 10.5px; letter-spacing: 3.2px; line-height: 1.2; }
  .card--front .wordmark { right: 22px; top: 28px; }
  .card--back .wordmark { left: 56px; top: 30px; }

  .banner {
    position: absolute; background: var(--teal); color: var(--paper);
    font-family: "Baloo 2", "Trebuchet MS", sans-serif; font-weight: 500;
    display: flex; align-items: center;
  }
  .banner--service {
    right: 0; top: 122px; width: 262px; height: 38px;
    clip-path: polygon(0 60%, 22px 0, 100% 0, 100% 100%, 22px 100%);
    justify-content: flex-end; padding-right: 26px; font-size: 23px;
  }
  .banner--classes {
    left: 0; top: 262px; width: 430px; height: 36px;
    clip-path: polygon(0 0, 380px 0, 100% 0, 390px 100%, 0 100%);
    padding-left: 205px; font-size: 19px; letter-spacing: .3px;
  }
  .banner--address {
    left: 0; top: 238px; width: 446px; height: 42px;
    clip-path: polygon(0 0, 400px 0, 100% 50%, 400px 100%, 0 100%);
    padding-left: 22px; font-size: 18px; letter-spacing: .4px;
  }

  .schedule { position: absolute; left: 222px; right: 26px; top: 170px; list-style: none; }
  .schedule__item {
    text-align: right; font-size: 14.5px; line-height: 21px;
    border-bottom: 1.5px solid var(--rule); padding-right: 4px;
  }

  .contact { position: absolute; left: 24px; top: 194px; display: flex; gap: 38px;
    font-size: 15px; color: var(--ink); }
  .contact__item { display: flex; align-items: center; gap: 8px; }
  .contact__item--web { font-family: "Baloo 2", "Trebuchet MS", sans-serif; font-weight: 500; font-size: 17px; }
  .contact__icon { width: 18px; height: 18px; flex: none; }
</style>
</head>
<body>
<main class="stage">

  <section class="card card--front" aria-label="Card front: service times">
    <div class="side-panel"><div class="side-panel__disc"></div></div>
    <div class="wordmark">
      <span class="wordmark__dot"></span>
      <div>
        <div class="wordmark__name">BROOKVANE</div>
        <div class="wordmark__sub">PENTECOSTAL CHURCH</div>
      </div>
    </div>
    <div class="banner banner--service">Service times</div>
    <ul class="schedule">
      <li class="schedule__item">Sunday - 10am Sunday School</li>
      <li class="schedule__item">11am Family Worship</li>
      <li class="schedule__item">6pm Night of Prayer</li>
      <li class="schedule__item">Wednesday - 7:30pm Adult Bible Study</li>
    </ul>
    <div class="banner banner--classes">Classes for all ages......</div>
  </section>

  <section class="card card--back" aria-label="Card back: contact details">
    <div class="side-panel"><div class="side-panel__disc"></div></div>
    <div class="wordmark">
      <span class="wordmark__dot"></span>
      <div>
        <div class="wordmark__name">BROOKVANE</div>
        <div class="wordmark__sub">PENTECOSTAL CHURCH</div>
      </div>
    </div>
    <div class="contact">
      <span class="contact__item">
        <svg class="contact__icon" viewBox="0 0 20 20" aria-hidden="true">
          <circle cx="10" cy="10" r="10" fill="#4f8e9e"/>
          <path d="M6.5 5.5c.6-.6 1.4-.5 1.8.1l.9 1.5c.3.5.2 1-.2 1.4l-.6.5c.6 1.3 1.6 2.3 2.9 2.9l.5-.6c.4-.4 1-.5 1.4-.2l1.5.9c.6.4.7 1.2.1 1.8l-.7.7c-3.4.4-8-4.2-7.6-7.6z" fill="#fff"/>
        </svg>
        815-555-0163
      </span>
      <span class="contact__item contact__item--web">
        <svg class="contact__icon" viewBox="0 0 20 20" aria-hidden="true" fill="none" stroke="#7fa9b5" stroke-width="1.4">
          <circle cx="10" cy="10" r="8.5"/>
          <ellipse cx="10" cy="10" rx="3.8" ry="8.5"/>
          <path d="M1.5 10h17M3 5.5h14M3 14.5h14"/>
        </svg>
        brookvane.example
      </span>
    </div>
    <div class="banner banner--address">2718 Maple Row, Rockford, IL 61142</div>
  </section>

</main>
</body>
</html>
```